QLM Stationery Design Project

Dear Designers,
We need a new stationery design for company to match our new logo.
Designers should provide a design for the following:
1. Business Card: 3.5x2 Inches.
2. Letterhead: A4 size.
3. Envelops: 25x35.5 Cm.
You can keep the Arabic name at the bottom of the logo Or you can use the separate attached Arabic Name.
Please refer to the attached logo guide for design information.
Sample Business Card information:
Name: Tariq Saleem
Position: Operation Manager
Tel: +000 0000 4717 Ex. 500
Fax: +000 (0)000 2153
Mob: +000 (0)000 7260
email: tariq@qlm-example.com.sa
URL: www.qlm-example.com.sa
Address:
Sample Tower, Suite 517
Example Road 12
Khobar, 00000
Saudi Arabia
Updates
Dear All,
Please note, we had uploaded our logo along with Arabic writing in Adobe illustrator format (.ai).
Regards,
Yousef
Dear All,
A sample data for the business card had been added as per your request.
Regards,
Yousef

```html
<!DOCTYPE html>
<html lang="en">
<head>
<meta charset="utf-8">
<title>QLM Stationery Design</title>
<link href="https://fonts.googleapis.com/css2?family=Open+Sans:wght@400;600;700&display=swap" rel="stylesheet">
<style>
:root{
  --navy:#0c3766;
  --navy-dark:#04203f;
  --band:#e4e5e7;
  --band-dark:#9a9b9e;
  --paper:#ffffff;
  --ground:#e9eaec;
  --ink:#3c3f44;
  --muted:#5a5d62;
}
*{box-sizing:border-box;margin:0;padding:0}
html,body{width:1200px;height:861px;overflow:hidden}
body{background:var(--ground);font-family:"Open Sans",sans-serif;position:relative;color:var(--ink)}

.wordmark{font-weight:700;color:var(--navy);letter-spacing:.5px;line-height:1;display:flex;align-items:center;gap:5px;white-space:nowrap}
.wordmark .dot{display:inline-block;background:var(--navy);border-radius:50%;flex:none}

.letterhead{position:absolute;left:140px;top:110px;width:340px;height:440px;background:var(--paper);box-shadow:0 2px 8px rgba(0,0,0,.15)}
.letterhead .header-band{position:absolute;left:120px;right:0;top:38px;height:26px;background:linear-gradient(90deg,#f2f2f3,var(--band))}
.letterhead .wordmark{position:absolute;left:30px;top:39px;font-size:22px}
.letterhead .wordmark .dot{width:10px;height:10px}
.letterhead .footer-text{position:absolute;right:24px;bottom:24px;font-size:6px;color:var(--muted);white-space:nowrap}
.letterhead .footer-band{position:absolute;left:0;right:0;bottom:0;height:14px;background:linear-gradient(90deg,var(--band-dark),var(--band))}

.envelope{position:absolute;left:545px;top:185px;width:570px;height:575px;background:var(--paper);box-shadow:0 2px 8px rgba(0,0,0,.15)}
.envelope .flap{position:absolute;left:0;right:0;top:0;height:168px;background:linear-gradient(100deg,var(--navy-dark),var(--navy) 90%);border-radius:0 0 14px 14px}

.card{position:absolute;top:590px;width:180px;height:103px;box-shadow:0 2px 6px rgba(0,0,0,.2);overflow:hidden}
.card-front{left:140px;background:var(--paper)}
.card-front .header-band{position:absolute;left:70px;right:0;top:12px;height:13px;background:var(--band)}
.card-front .wordmark{position:absolute;left:10px;top:12px;font-size:13px}
.card-front .wordmark .dot{width:6px;height:6px}
.card-front .contact{position:absolute;left:10px;top:38px;width:98px;list-style:none;font-size:4.2px;line-height:6.3px;color:var(--muted)}
.card-front .contact li{display:flex;align-items:center;gap:3px;white-space:nowrap}
.card-front .contact i{display:inline-block;width:3.5px;height:3.5px;background:var(--navy);border-radius:50%;flex:none}
.card-front .person{position:absolute;left:114px;top:44px}
.card-front .person .name{font-size:7.5px;font-weight:700;color:var(--navy);white-space:nowrap}
.card-front .person .role{font-size:4.8px;color:var(--muted);white-space:nowrap}
.card-front .bottom-band{position:absolute;right:0;bottom:6px;width:90px;height:10px}

.card-back{left:340px;background:linear-gradient(120deg,var(--navy-dark),var(--navy));display:flex;align-items:center;justify-content:center}
.card-back .wordmark{color:#fff;font-size:22px}
.card-back .wordmark .dot{width:9px;height:9px;background:#fff}
</style>
</head>
<body>
<section class="letterhead" aria-label="Letterhead">
  <div class="header-band"></div>
  <div class="wordmark"><span class="dot"></span>QLM</div>
  <p class="footer-text">Khobar 00000, Saudi Arabia · www.qlm-example.com.sa</p>
  <div class="footer-band"></div>
</section>

<section class="envelope" aria-label="Envelope">
  <div class="flap"></div>
</section>

<section class="card card-front" aria-label="Business card front">
  <div class="header-band"></div>
  <div class="wordmark"><span class="dot"></span>QLM</div>
  <ul class="contact">
    <li><i></i>Sample Tower, Suite 517, Example Road 12</li>
    <li><i></i>Khobar, 00000, Saudi Arabia</li>
    <li><i></i>+000 0000 4717 Ex. 500</li>
    <li><i></i>+000 (0)000 2153</li>
    <li><i></i>+000 (0)000 7260</li>
    <li><i></i>tariq@qlm-example.com.sa</li>
    <li><i></i>www.qlm-example.com.sa</li>
  </ul>
  <div class="person">
    <p class="name">Tariq Saleem</p>
    <p class="role">Operation Manager</p>
  </div>
  <svg class="bottom-band" viewBox="0 0 90 10" preserveAspectRatio="none" aria-hidden="true">
    <polygon points="8,0 90,0 90,10 8,10 0,5" fill="#0c3766"/>
  </svg>
</section>

<section class="card card-back" aria-label="Business card back">
  <div class="wordmark"><span class="dot"></span>QLM</div>
</section>
</body>
</html>
```